Kestrel Bridge Consulting (KBC) Business Card Design

I would like to create double-sided business cards that contain:
1) Name: Derek Molvane
2) Phone Number: +1 (555) 218-4907
3) Email: Derek.Molvane@KestrelBridgeConsulting.example
4) Website: KestrelBridgeConsulting.example

I would like to include my logo and a color scheme similar to the Varnholt Grand Prix Ostera squad color scheme (black, silver, greenish-blue – but can also include regular blue)

What we do: Our company develops and delivers innovative and pragmatic information technology and cybersecurity risk and compliance solutions for organizations in the commercial market as well as the federal, and state/local sectors.

```html
<!DOCTYPE html>
<html lang="en">
<head>
<meta charset="utf-8">
<title>Kestrel Bridge Consulting – Business Card</title>
<link rel="stylesheet" href="https://fonts.googleapis.com/css2?family=Exo+2:wght@400&family=Montserrat:wght@600;800&display=swap">
<style>
  :root {
    --page: #e6e8e7;
    --card-core: #333333;
    --card-edge: #080808;
    --teal: #34c0b8;
    --blue: #0e6fb5;
    --white: #ffffff;
    --ink: #0b1416;
  }
  * { margin: 0; padding: 0; box-sizing: border-box; }
  html, body {
    width: 1200px; height: 1200px; overflow: hidden;
    background: var(--page);
  }
  .sheet { position: relative; width: 1200px; height: 1200px; }

  .card {
    position: absolute;
    left: 186px;
    width: 828px;
    height: 459px;
    overflow: hidden;
    background: radial-gradient(ellipse 60% 70% at 50% 45%, var(--card-core) 0%, #1a1a1a 55%, var(--card-edge) 100%);
  }
  .card--front { top: 96px; }
  .card--back { top: 634px; }

  /* Front */
  .brand {
    position: absolute;
    left: 218px; top: 134px;
    display: flex; align-items: center; gap: 26px;
  }
  .brand__dot {
    width: 92px; height: 92px; border-radius: 50%;
    background: var(--teal);
  }
  .brand__name {
    font-family: "Exo 2", sans-serif;
    font-weight: 400;
    font-size: 33px;
    line-height: 36px;
    letter-spacing: 1px;
    color: var(--white);
    text-transform: uppercase;
  }
  .band { position: absolute; top: 341px; height: 26px; }
  .band--site { left: 0; width: 517px; background: var(--teal); }
  .band--mid { left: 530px; width: 192px; background: var(--blue); }
  .band--end { left: 737px; width: 91px; background: var(--teal); }
  .website {
    position: absolute; left: 131px; top: 341px; height: 26px;
    display: flex; align-items: center;
    font-family: "Montserrat", sans-serif; font-weight: 800;
    font-size: 16px; color: var(--ink); text-transform: uppercase;
  }

  /* Back */
  .rail { position: absolute; left: 56px; width: 41px; }
  .rail--top { top: 0; height: 112px; background: var(--blue); }
  .rail--marker { top: 126px; height: 35px; background: var(--teal); }
  .rail--bottom { top: 174px; height: 285px; background: var(--blue); }
  .person {
    position: absolute; left: 116px; top: 120px;
    font-family: "Montserrat", sans-serif; font-weight: 800;
    font-size: 36px; color: var(--teal); text-transform: uppercase;
    letter-spacing: 0.5px;
  }
  .contact {
    position: absolute; left: 61px;
    display: flex; align-items: center; gap: 23px;
    font-family: "Montserrat", sans-serif; font-weight: 600;
    font-size: 19px; color: var(--teal);
  }
  .contact--phone { top: 271px; }
  .contact--email { top: 330px; }
  .contact__icon { width: 32px; height: 32px; flex: none; }
</style>
</head>
<body>
<main class="sheet">
  <section class="card card--front" aria-label="Card front">
    <div class="brand">
      <div class="brand__dot" aria-hidden="true"></div>
      <div class="brand__name">Kestrel<br>Bridge<br>Consulting</div>
    </div>
    <div class="band band--site"></div>
    <div class="band band--mid"></div>
    <div class="band band--end"></div>
    <div class="website">KestrelBridgeConsulting.example</div>
  </section>

  <section class="card card--back" aria-label="Card back">
    <div class="rail rail--top"></div>
    <div class="rail rail--marker"></div>
    <div class="rail rail--bottom"></div>
    <h1 class="person">Derek Molvane</h1>

    <div class="contact contact--phone">
      <svg class="contact__icon" viewBox="0 0 32 32" aria-hidden="true">
        <circle cx="16" cy="16" r="16" fill="#ffffff"/>
        <path d="M11.2 8.5l2.4-.4 1.5 4-1.6 1.4c.9 2 2.6 3.7 4.6 4.6l1.4-1.6 4 1.5-.4 2.4c-.2 1-1.1 1.7-2.1 1.6C14.6 21.5 10.5 17.4 9.9 10.6c-.1-1 .6-1.9 1.3-2.1z" fill="#0e6fb5"/>
      </svg>
      <span>+1 (555) 218-4907</span>
    </div>

    <div class="contact contact--email">
      <svg class="contact__icon" viewBox="0 0 32 32" aria-hidden="true">
        <circle cx="16" cy="16" r="16" fill="#ffffff"/>
        <rect x="8" y="10.5" width="16" height="11" rx="1" fill="none" stroke="#0e6fb5" stroke-width="1.8"/>
        <path d="M8.5 11.5l7.5 6 7.5-6" fill="none" stroke="#0e6fb5" stroke-width="1.8"/>
      </svg>
      <span>Derek.Molvane@KestrelBridgeConsulting.example</span>
    </div>
  </section>
</main>
</body>
</html>
```